DL Flyer for garden consultants. I will supply text and logo

To design an eye catching but simple, uncluttered flyer for letter box distribution. The text and logo are provided.

```html
<!DOCTYPE html>
<html lang="en">
<head>
<meta charset="utf-8">
<title>Fernway Garden Advisors – DL Flyer</title>
<link rel="stylesheet" href="https://fonts.googleapis.com/css2?family=Arimo:ital,wght@0,400;0,700;1,400&display=swap">
<style>
  :root {
    --stage: #000000;
    --label: #9a9a9a;
    --green-deep: #1d5e31;
    --green-mid: #2ea64a;
    --green-bright: #4bb848;
    --lime: #a9cd3c;
    --yellow: #f2ec1c;
    --paper: #edf6e5;
    --white: #ffffff;
  }
  * { margin: 0; padding: 0; box-sizing: border-box; }
  html, body {
    width: 1200px; height: 854px; overflow: hidden;
    background: var(--stage);
    font-family: "Arimo", Arial, sans-serif;
  }
  .sheet { position: relative; width: 1200px; height: 854px; }
  .side-label {
    position: absolute; top: 15px; width: 528px; text-align: center;
    color: var(--label); font-size: 16px; letter-spacing: 0.5px;
  }
  .side { position: absolute; top: 45px; width: 528px; height: 767px; overflow: hidden; }
  .side-front {
    left: 40px;
    background:
      radial-gradient(ellipse 70% 55% at 95% 72%, rgba(222,228,40,0.95), rgba(222,228,40,0) 70%),
      linear-gradient(160deg, #47b649 0%, #5dbb46 45%, #8cc63f 75%, #c5da33 100%);
  }
  .side-back { left: 636px; background: var(--paper); }

  .teaser {
    position: absolute; top: 72px; left: 0; width: 528px;
    color: var(--white); text-align: center; line-height: 1;
  }
  .teaser p { margin-bottom: 6px; }
  .teaser .small { font-size: 26px; }
  .teaser .big { font-size: 44px; }
  .teaser .l1 { padding-left: 30px; }
  .teaser .l3 { padding-left: 10px; }
  .teaser-answer {
    position: absolute; top: 218px; left: 166px;
    color: var(--yellow); font-style: italic; font-size: 42px;
  }
  .front-url {
    position: absolute; bottom: 26px; left: 29px;
    color: var(--green-deep); font-size: 16px;
  }

  .brand {
    position: absolute; top: 92px; left: 62px;
    display: flex; align-items: center; gap: 22px;
  }
  .brand-dot { width: 78px; height: 78px; border-radius: 50%; background: var(--green-mid); }
  .brand-name { color: var(--lime); font-weight: 400; line-height: 1.05; }
  .brand-name .n1 { display: block; font-size: 58px; }
  .brand-name .n2 { display: block; font-size: 20px; letter-spacing: 4px; text-transform: uppercase; }

  .tagline {
    position: absolute; top: 290px; left: 61px;
    color: var(--green-mid); font-style: italic; font-size: 40px;
  }
  .services { position: absolute; top: 372px; left: 42px; width: 440px; list-style: none; }
  .services li { position: relative; padding-left: 36px; margin-bottom: 23px; }
  .services li::before {
    content: ""; position: absolute; left: 2px; top: 7px;
    width: 6px; height: 6px; border-radius: 50%; background: var(--green-deep);
  }
  .service-name { display: block; color: var(--green-deep); font-size: 17px; line-height: 22px; }
  .service-note { display: block; color: var(--green-mid); font-style: italic; font-size: 16.5px; line-height: 22px; }

  .back-footer {
    position: absolute; left: 0; bottom: 0; width: 528px; height: 57px;
    background: linear-gradient(90deg, #66bd4b 0%, #8ec85a 60%, #b6d873 100%);
    color: var(--green-deep); font-size: 17px;
    display: flex; align-items: center; justify-content: center;
  }
</style>
</head>
<body>
<main class="sheet">
  <div class="side-label" style="left:40px">SIDE - 1</div>
  <div class="side-label" style="left:636px">SIDE - 2</div>

  <section class="side side-front">
    <div class="teaser">
      <p class="l1"><span class="small">Have </span><span class="big">you</span></p>
      <p><span class="small">been </span><span class="big">thinking</span><span class="small"> about</span></p>
      <p class="l3"><span class="small">your </span><span class="big">garden</span><span class="small"> lately?</span></p>
    </div>
    <div class="teaser-answer">Well.....</div>
    <div class="front-url">www.fernwaygardenadvisors.com.au</div>
  </section>

  <section class="side side-back">
    <div class="brand">
      <span class="brand-dot"></span>
      <span class="brand-name"><span class="n1">Fernway</span><span class="n2">Garden Advisors</span></span>
    </div>
    <div class="tagline">.....we can help.</div>
    <ul class="services">
      <li>
        <span class="service-name">Garden Assessment Consultation and Report</span>
        <span class="service-note">...... information vital to ensuring your dream becomes reality!</span>
      </li>
      <li>
        <span class="service-name">Pre Sale Consultation and Report</span>
        <span class="service-note">….. maximise your sale dollar!</span>
      </li>
      <li>
        <span class="service-name">Develop a Plant Portfolio</span>
        <span class="service-note">….. successfully navigate the plant maze!</span>
      </li>
    </ul>
    <footer class="back-footer">Check us out at:&nbsp; www.fernwaygardenadvisors.com.au</footer>
  </section>
</main>
</body>
</html>
```